Varneck Bidding Business Cards Design Needed

I need a business card design that is modern looking - double sided (maybe just my logo on the back, but open to suggestions) - the overall design is up to you. I want it to be easy to read - not over the top flashy. I already have a company logo which I uploaded so that needs to be used. The colors of my logo are the colors I want on the card... so blue and gray (do need to match the logo colors).

Requirements
Must have
• Would like the card to be sleek, modern and easy to ready

```html
<!DOCTYPE html>
<html lang="en">
<head>
<meta charset="utf-8">
<title>Varneck Bidding – Business Cards</title>
<link href="https://fonts.googleapis.com/css2?family=Roboto:wght@400;500;700&display=swap" rel="stylesheet">
<style>
  :root {
    --bg: #e9e7e3;
    --paper: #f4f4f4;
    --blue: #2e8fc6;
    --blue-dark: #1f78ad;
    --gray: #5d5e61;
    --gray-dark: #48494c;
    --white: #ffffff;
    --ink-soft: #e2e2e2;
  }
  * { box-sizing: border-box; margin: 0; padding: 0; }
  html, body { width: 1200px; height: 780px; overflow: hidden; }
  body {
    background: var(--bg);
    font-family: "Roboto", Arial, sans-serif;
    position: relative;
  }
  .card {
    position: absolute;
    width: 560px;
    height: 320px;
    border-radius: 16px;
    overflow: hidden;
    box-shadow: 0 10px 28px rgba(0,0,0,0.22);
  }
  /* Front */
  .card-front { left: 30px; top: 90px; background: var(--paper); }
  .front-white {
    position: absolute; left: 0; top: 0; width: 100%; height: 150px;
    background: linear-gradient(180deg, #fafafa, #ececec);
  }
  .social {
    position: absolute; right: 26px; top: 20px; display: flex; gap: 6px;
  }
  .social span {
    width: 24px; height: 24px; border-radius: 50%;
    border: 2px solid var(--blue); background: var(--white);
  }
  .brand {
    position: absolute; left: 40px; top: 62px;
    display: flex; align-items: center; gap: 16px;
  }
  .brand-square {
    width: 52px; height: 52px; background: var(--blue);
  }
  .brand-name {
    font-weight: 700; font-size: 40px; letter-spacing: 1px;
    color: var(--blue); text-transform: uppercase;
  }
  .front-band {
    position: absolute; left: 0; top: 150px; width: 100%; height: 36px;
    background: linear-gradient(180deg, var(--blue), var(--blue-dark));
    display: flex; align-items: center; padding-left: 40px;
    color: var(--white);
  }
  .person-name { font-size: 19px; font-weight: 500; }
  .divider { margin: 0 12px; font-size: 20px; opacity: 0.9; }
  .person-role { font-size: 13px; }
  .front-gray {
    position: absolute; left: 0; top: 186px; width: 100%; height: 134px;
    background: linear-gradient(180deg, var(--gray), var(--gray-dark));
    padding: 18px 0 0 40px;
  }
  .contact-list { list-style: none; }
  .contact-list li {
    display: flex; align-items: center; gap: 10px;
    color: var(--ink-soft); font-size: 14px; line-height: 24px;
  }
  .contact-icon {
    width: 16px; height: 16px; border-radius: 50%;
    background: var(--blue); display: flex; align-items: center; justify-content: center;
  }
  .contact-icon svg { width: 10px; height: 10px; }

  /* Back */
  .card-back {
    left: 610px; top: 370px;
    background: linear-gradient(180deg, #616265, var(--gray-dark));
    display: flex; flex-direction: column; align-items: center; justify-content: center;
    gap: 14px;
  }
  .back-brand { display: flex; align-items: center; gap: 16px; }
  .back-brand .brand-square { background: var(--white); width: 46px; height: 46px; }
  .back-brand .brand-name { color: var(--white); font-size: 38px; }
  .tagline { color: var(--ink-soft); font-size: 15px; letter-spacing: 0.5px; }
</style>
</head>
<body>
  <section class="card card-front" aria-label="Business card front">
    <div class="front-white">
      <div class="social" aria-label="Social profiles">
        <span></span><span></span><span></span>
      </div>
      <div class="brand">
        <div class="brand-square"></div>
        <div class="brand-name">Varneck Bidding</div>
      </div>
    </div>
    <div class="front-band">
      <span class="person-name">Corin Halvey</span>
      <span class="divider">|</span>
      <span class="person-role">Owner/President - Auctioneer</span>
    </div>
    <div class="front-gray">
      <ul class="contact-list">
        <li><span class="contact-icon"><svg viewBox="0 0 10 10"><path d="M2 1h2l1 2-1 1c.6 1.2 1.5 2 2.5 2.5l1-1 2 1v2c-4.5 0-8.5-4-8.5-7.5z" fill="#fff"/></svg></span>555-301-7742</li>
        <li><span class="contact-icon"><svg viewBox="0 0 10 10"><rect x="1" y="2.5" width="8" height="5" fill="none" stroke="#fff"/><path d="M1 2.5l4 3 4-3" fill="none" stroke="#fff"/></svg></span>varneckbidding@inboxmail.net</li>
        <li><span class="contact-icon"><svg viewBox="0 0 10 10"><circle cx="5" cy="5" r="3.8" fill="none" stroke="#fff"/><path d="M1.2 5h7.6M5 1.2c-2 2.5-2 5.1 0 7.6M5 1.2c2 2.5 2 5.1 0 7.6" fill="none" stroke="#fff" stroke-width=".7"/></svg></span>bidrelaydesk.com</li>
        <li><span class="contact-icon"><svg viewBox="0 0 10 10"><path d="M5 9.2C3 6.5 2 5 2 3.8a3 3 0 016 0C8 5 7 6.5 5 9.2z" fill="#fff"/><circle cx="5" cy="3.8" r="1" fill="#2e8fc6"/></svg></span>Alderbrook, WA</li>
      </ul>
    </div>
  </section>

  <section class="card card-back" aria-label="Business card back">
    <div class="back-brand">
      <div class="brand-square"></div>
      <div class="brand-name">Varneck Bidding</div>
    </div>
    <p class="tagline">Bright Benefit Bidding, Coast to Coast</p>
  </section>
</body>
</html>
```